Wordpress template re-design of current website

We need a WordPress template design and new look for our existing website. Our existing site it located at www.velmoro.com.au We are a tech company and want a fresh, clean modern website that matches our brand, services and logo colors. Our main Services are hospitality solutions, Velmoro TV solution and managed networks, more information on these can come from our existing website.

Target Market(s)

We are a tech company so must have a modern feel for new technology

Industry/Entity Type

It Company

Number of Pages Required

5+ page

Font styles to use
Sans Serif

Requirements
Must have
• Be based on a wordpress templete design and match the services that we have in our existing website, in the testimonials want a place for video testimonials as well as text. Nice clean icons used for graphics to represent services.
Nice to have
• nice visual representation of our services in the way of clean icons etc
Should not have
• Clutter

```html
<!DOCTYPE html>
<html lang="en">
<head>
<meta charset="utf-8">
<title>Velmoro Wireless — Creating Solutions that work</title>
<link rel="stylesheet" href="https://fonts.googleapis.com/css2?family=Source+Sans+3:wght@400;600;700&display=swap">
<style>
  :root {
    --brand-blue: #0b4a8b;
    --tagline-grey: #4d5259;
    --heading-ink: #2b2b2b;
    --body-grey: #4f4f4f;
    --page-bg: #ffffff;
  }
  * { box-sizing: border-box; margin: 0; padding: 0; }
  html, body {
    width: 1200px;
    height: 556px;
    overflow: hidden;
    background: var(--page-bg);
    font-family: "Source Sans 3", "Helvetica Neue", Arial, sans-serif;
  }
  .page {
    position: relative;
    width: 1200px;
    height: 556px;
  }
  .masthead {
    position: absolute;
    left: 112px;
    top: 62px;
  }
  .brand-name {
    font-size: 50px;
    font-weight: 700;
    color: var(--brand-blue);
    line-height: 1;
    letter-spacing: -0.2px;
  }
  .tagline {
    margin-top: 4px;
    font-size: 29px;
    font-weight: 400;
    color: var(--tagline-grey);
    line-height: 1.1;
  }
  .services {
    position: absolute;
    top: 248px;
    left: 0;
    width: 1200px;
    list-style: none;
  }
  .service {
    position: absolute;
    top: 0;
    width: 240px;
    margin-left: -120px;
    text-align: center;
  }
  .service--hotspots { left: 225px; }
  .service--tv { left: 475px; }
  .service--hsia { left: 724px; }
  .service--social { left: 976px; }
  .service-icon {
    height: 74px;
    display: flex;
    align-items: center;
    justify-content: center;
  }
  .service-icon svg { display: block; }
  .service-title {
    margin-top: 10px;
    font-size: 24px;
    font-weight: 700;
    color: var(--heading-ink);
    line-height: 1.2;
  }
  .service-text {
    margin: 10px auto 0;
    width: 200px;
    font-size: 11px;
    color: var(--body-grey);
    line-height: 14px;
  }
  .service--social .service-text { margin-top: 16px; }
</style>
</head>
<body>
<main class="page">
  <header class="masthead">
    <h1 class="brand-name">Velmoro Wireless</h1>
    <p class="tagline">Creating Solutions that work</p>
  </header>

  <ul class="services">
    <li class="service service--hotspots">
      <div class="service-icon">
        <svg width="82" height="60" viewBox="0 0 82 60" fill="none" stroke="var(--brand-blue)" stroke-width="6" stroke-linecap="round" aria-hidden="true">
          <path d="M4 19 A52 52 0 0 1 78 19"/>
          <path d="M15 30 A37 37 0 0 1 67 30"/>
          <path d="M26 41 A21 21 0 0 1 56 41"/>
          <circle cx="41" cy="54" r="3" fill="var(--brand-blue)" stroke="none"/>
        </svg>
      </div>
      <h2 class="service-title">Wi-Fi Hotspots</h2>
      <p class="service-text">Leading supplier of public access and internet billing systems.</p>
    </li>

    <li class="service service--tv">
      <div class="service-icon">
        <svg width="76" height="66" viewBox="0 0 76 66" fill="none" stroke="var(--brand-blue)" stroke-width="4.5" aria-hidden="true">
          <rect x="3" y="3" width="70" height="47" rx="3"/>
          <line x1="3" y1="41" x2="73" y2="41"/>
          <line x1="38" y1="50" x2="38" y2="61"/>
          <line x1="24" y1="62" x2="52" y2="62" stroke-linecap="round"/>
        </svg>
      </div>
      <h2 class="service-title">Velmoro TV</h2>
      <p class="service-text">Turn you standard TV into a full guest information system and point of sale.</p>
    </li>

    <li class="service service--hsia">
      <div class="service-icon">
        <svg width="68" height="68" viewBox="0 0 68 68" fill="none" stroke="var(--brand-blue)" aria-hidden="true">
          <rect x="2" y="2" width="64" height="64" stroke-width="4"/>
          <path d="M23 20 V48 M45 20 V48 M23 34 H45" stroke-width="3"/>
        </svg>
      </div>
      <h2 class="service-title">HSIA Solutions</h2>
      <p class="service-text">Our guest acceess solutions have been built with the guest in mind and are easy to use</p>
    </li>

    <li class="service service--social">
      <div class="service-icon">
        <svg width="42" height="72" viewBox="0 0 42 72" aria-hidden="true">
          <rect x="0" y="0" width="42" height="72" rx="4" fill="var(--brand-blue)"/>
          <rect x="4" y="8" width="34" height="54" fill="var(--page-bg)"/>
          <line x1="16" y1="4" x2="26" y2="4" stroke="var(--page-bg)" stroke-width="1.5"/>
          <circle cx="21" cy="67" r="2.5" fill="var(--page-bg)"/>
          <g fill="none" stroke="var(--brand-blue)" stroke-width="2.2" stroke-linecap="round">
            <path d="M11 30 A15 15 0 0 1 31 30"/>
            <path d="M14.5 34 A10 10 0 0 1 27.5 34"/>
            <path d="M18 38 A4.5 4.5 0 0 1 24 38"/>
          </g>
          <circle cx="21" cy="41" r="1.4" fill="var(--brand-blue)"/>
        </svg>
      </div>
      <h2 class="service-title">Social Wi-Fi</h2>
      <p class="service-text">Get more out of your existing Wi-Fi with our social plug-ins to gain valuble insight into users</p>
    </li>
  </ul>
</main>
</body>
</html>
```